Label Design Brief - Quillmere Health
Label Panel Dimensions 1.25" W x 2.375" H (front/back panel)
Hello - our company develops novel products for the skin, & hair care industry as well as dietary supplements. We're looking for a label design for a new product. The product is a premium Topical hair loss/growth serum. I attached the brand logo & 2 other sister products along with some competitive products.
The product is a topical natural hair loss serum for men & women to regrow new hair and help restore hair loss & thinning hair due to vitamin deficiencies, hormone imbalance & aging. It is a science based efficacious serum with a century’s old medicinal herbal formula.
Attached is our logo & some files of other competition. The label must have an upscale, technology flair to it. The product is clinically effective, leveraged by Ancient Wisdom and Modern Science.
Below are attached files of 2 of our products & other generic competition for your perusal.

https://www.shopvarnel.example/item/K7T2QPL4XR?src=listing_offer

https://www.shopvarnel.example/item/K7T5MDR9WA/src=alt-list-view?vw=1&src=listing_lowcost

Target Market(s)

men & women age 18-80

Requirements
Must have
• see brief
Should not have
• Please do not have a picture of a man or a women on the label.

```html
<!DOCTYPE html>
<html lang="en">
<head>
<meta charset="utf-8">
<title>Quillmere Health – DHT Blocker Growth Activator Label</title>
<link rel="stylesheet" href="https://fonts.googleapis.com/css2?family=Roboto+Condensed:wght@700;900&family=Caveat:wght@600&display=swap">
<style>
  :root {
    --page: #ffffff;
    --label-bg: #f3f2f1;
    --label-edge: #d9d6d3;
    --brown: #6b3a1f;
    --brown-dark: #3d2112;
    --orange: #d9772b;
    --white: #ffffff;
    --hair-dark: #1c130e;
    --hair-mid: #4a3020;
    --skin: #9a6a4a;
  }
  * { margin: 0; padding: 0; box-sizing: border-box; }
  html, body {
    width: 1200px;
    height: 1200px;
    overflow: hidden;
    background: var(--page);
  }
  .canvas {
    position: relative;
    width: 1200px;
    height: 1200px;
  }
  .label {
    position: absolute;
    left: 320px;
    top: 108px;
    width: 560px;
    height: 985px;
    background: var(--label-bg);
    border: 2px solid var(--label-edge);
    border-radius: 26px;
    overflow: hidden;
    font-family: "Roboto Condensed", "Arial Narrow", sans-serif;
  }
  .band-top, .band-bottom {
    position: absolute;
    left: 0;
    width: 100%;
  }
  .band-top { top: 0; }
  .band-bottom { bottom: 0; }

  .brand {
    position: absolute;
    top: 150px;
    left: 0;
    width: 100%;
    display: flex;
    justify-content: center;
    align-items: center;
    gap: 14px;
  }
  .brand-mark {
    width: 22px;
    height: 22px;
    border-radius: 50%;
    background: var(--brown);
  }
  .brand-name {
    font-weight: 700;
    font-size: 50px;
    letter-spacing: 1px;
    color: var(--brown);
    text-transform: uppercase;
    line-height: 1;
  }
  .tagline {
    position: absolute;
    top: 246px;
    left: 0;
    width: 100%;
    text-align: center;
    font-family: "Caveat", cursive;
    font-weight: 600;
    font-size: 30px;
    color: var(--brown-dark);
  }
  .claim-dht {
    position: absolute;
    left: 19px;
    top: 312px;
    width: 203px;
    height: 182px;
    background: var(--brown);
    color: var(--white);
    text-align: center;
    padding-top: 14px;
  }
  .claim-dht .big {
    display: block;
    font-weight: 900;
    font-size: 92px;
    line-height: 0.95;
  }
  .claim-dht .small {
    display: block;
    font-weight: 700;
    font-size: 38px;
    letter-spacing: 1px;
    line-height: 1.1;
  }
  .claim-growth {
    position: absolute;
    left: 233px;
    top: 312px;
    width: 294px;
    height: 182px;
    background: var(--brown);
    color: var(--white);
    padding: 14px 0 0 14px;
  }
  .claim-growth .line {
    display: block;
    font-weight: 900;
    font-size: 52px;
    line-height: 0.98;
    letter-spacing: 1px;
  }
  .claim-growth .audience {
    display: block;
    margin-top: 8px;
    font-weight: 700;
    font-size: 26px;
    color: var(--orange);
    letter-spacing: 0.5px;
  }
  .model-photo {
    position: absolute;
    left: 233px;
    top: 494px;
    width: 327px;
    height: 443px;
    background:
      radial-gradient(ellipse at 78% 45%, var(--skin) 0%, rgba(154,106,74,0) 32%),
      radial-gradient(ellipse at 40% 50%, var(--hair-mid) 0%, var(--hair-dark) 60%, rgba(28,19,14,0) 100%);
    border-radius: 40% 0 0 30%;
  }
  .notes {
    position: absolute;
    left: 58px;
    top: 752px;
    font-weight: 700;
    font-size: 22px;
    line-height: 1.3;
    color: var(--brown-dark);
  }
  .herb-bowl {
    position: absolute;
    left: 23px;
    top: 848px;
    width: 112px;
    height: 62px;
    background: var(--orange);
    border-radius: 10px 10px 56px 56px;
  }
  .volume {
    position: absolute;
    left: 128px;
    top: 888px;
    width: 118px;
    height: 30px;
    background: var(--orange);
    border-radius: 15px;
    color: var(--white);
    font-weight: 700;
    font-size: 22px;
    line-height: 30px;
    text-align: center;
    letter-spacing: 1px;
  }
</style>
</head>
<body>
<div class="canvas">
  <section class="label">
    <svg class="band-top" width="560" height="60" viewBox="0 0 560 60" aria-hidden="true">
      <path d="M0 0 H560 V33 H408 V42 Q408 56 394 56 H166 Q152 56 152 42 V33 H0 Z" fill="var(--brown)"/>
    </svg>

    <div class="brand">
      <span class="brand-mark"></span>
      <span class="brand-name">Quillmere Health</span>
    </div>

    <p class="tagline">A premium Topical hair loss/growth serum</p>

    <div class="claim-dht">
      <span class="big">DHT</span>
      <span class="small">BLOCKER</span>
    </div>

    <div class="claim-growth">
      <span class="line">GROWTH</span>
      <span class="line">ACTIVATOR</span>
      <span class="audience">FOR MEN &amp; WOMEN</span>
    </div>

    <div class="model-photo" role="img" aria-label="Photo area: model with long, voluminous dark curly hair"></div>

    <p class="notes">Lorem Ipsum<br>Lorem Ipsum</p>

    <div class="herb-bowl" role="img" aria-label="Illustration area: herbal mortar and pestle"></div>
    <div class="volume">2 FL OZ</div>

    <svg class="band-bottom" width="560" height="40" viewBox="0 0 560 40" aria-hidden="true">
      <rect x="0" y="4" width="560" height="36" fill="var(--brown)"/>
    </svg>
  </section>
</div>
</body>
</html>
```